Stationary/business card/envelope design for Larkvale Dentalcare

We are located in the foothills of the sierra nevada mountains. We are looking for a beautiful classy modern stationary. We need evelopes and business card design all to flow seamlessly. Envelope design.

Additional office address 4816 Meridian Wy., Suite B, Auburn, CA 95604 Phone: pending Fax: pending.

3 different Drs on each business card:
Helen R. Marsh, DDS
Orla P. Marsh, DDS
Rebecca S. Halvey, DDS

Target Market(s)

Dental patients

Industry/Entity Type

Dental

Contact Information for Business Card

Two sided. See example.

Font styles to use
Sans Serif

Requirements
Must have
• One sided business cards. Need envelope design.
Colors should match existing logo.

Helen R. Marsh, DDS
Orla P. Marsh, DDS
Rebecca S. Halvey, DDS

```html
<!DOCTYPE html>
<html lang="en">
<head>
<meta charset="utf-8">
<title>Larkvale Dentalcare – Business Card</title>
<link rel="stylesheet" href="https://fonts.googleapis.com/css2?family=Tinos:ital,wght@0,400;0,700;1,400;1,700&display=swap">
<style>
  :root {
    --bg: #ecebe8;
    --card: #ffffff;
    --ink: #1f1f1f;
    --green: #1d6b34;
    --blue: #2aa3cf;
    --rule: #2a2a2a;
  }
  * { margin: 0; padding: 0; box-sizing: border-box; }
  html, body { width: 1200px; height: 959px; overflow: hidden; }
  body {
    background: var(--bg);
    font-family: "Tinos", "Times New Roman", serif;
    color: var(--ink);
    display: flex;
    align-items: center;
    justify-content: center;
    gap: 80px;
  }
  .card {
    width: 420px;
    height: 735px;
    background: var(--card);
    box-shadow: 0 2px 10px rgba(0,0,0,0.12);
    position: relative;
  }

  /* Appointment side */
  .appointment { padding: 70px 48px 0; font-size: 19px; }
  .appointment .blank-line { border-bottom: 1.5px solid var(--rule); height: 34px; }
  .appointment .heading { margin-top: 8px; letter-spacing: 0.5px; }
  .slot-list { list-style: none; margin-top: 34px; }
  .slot {
    display: flex; align-items: flex-end; gap: 8px;
    height: 58px; font-style: italic;
  }
  .slot .day { width: 48px; }
  .slot .date { flex: 1; border-bottom: 1.5px solid var(--rule); }
  .slot .at { font-style: normal; }
  .slot .time { width: 66px; border-bottom: 1.5px solid var(--rule); }
  .notice { margin-top: 44px; line-height: 1.45; text-transform: uppercase; font-size: 18px; }
  .back-sign { margin-top: 30px; font-weight: 700; font-style: italic; font-size: 21px; }
  .back-contact { margin-top: 10px; font-size: 15.5px; line-height: 1.6; }

  /* Front side */
  .front { padding: 70px 40px 0; text-align: center; }
  .brand { display: flex; align-items: center; justify-content: center; gap: 14px; }
  .brand-dot { width: 64px; height: 64px; border-radius: 50%; background: var(--blue); }
  .brand-name { font-size: 30px; font-weight: 700; color: var(--green); }
  .doctor {
    margin-top: 46px; font-size: 33px; font-weight: 700; font-style: italic; color: var(--green);
  }
  .specialty { margin-top: 6px; font-size: 20px; font-weight: 700; font-style: italic; color: var(--blue); }
  .icon-row { display: flex; justify-content: center; gap: 10px; margin-top: 24px; }
  .icon-row svg { width: 20px; height: 20px; fill: var(--green); }
  .contact-list { list-style: none; margin-top: 12px; font-size: 21px; line-height: 1.42; }
  .divider { width: 28px; height: 3px; background: var(--green); margin: 8px auto; }
</style>
</head>
<body>

<section class="card appointment" aria-label="Appointment side">
  <div class="blank-line"></div>
  <p class="heading">HAS AN APPOINTMENT ON</p>
  <ul class="slot-list">
    <li class="slot"><span class="day">Mon</span><span class="date"></span><span class="at">AT</span><span class="time"></span></li>
    <li class="slot"><span class="day">Tues</span><span class="date"></span><span class="at">AT</span><span class="time"></span></li>
    <li class="slot"><span class="day">Wed</span><span class="date"></span><span class="at">AT</span><span class="time"></span></li>
    <li class="slot"><span class="day">Thu</span><span class="date"></span><span class="at">AT</span><span class="time"></span></li>
    <li class="slot"><span class="day">Fri</span><span class="date"></span><span class="at">AT</span><span class="time"></span></li>
  </ul>
  <p class="notice">If unable to keep appointment<br>kindly give 24 hour notice</p>
  <p class="back-sign">Helen Marsh, DDS</p>
  <p class="back-contact">Office: (916) 555-0142 &nbsp;Fax: (916) 555-0178<br>www.larkvaledentalcare.com</p>
</section>

<section class="card front" aria-label="Contact side">
  <div class="brand">
    <span class="brand-dot"></span>
    <span class="brand-name">Larkvale Dentalcare</span>
  </div>
  <h1 class="doctor">Helen R. Marsh, DDS</h1>
  <p class="specialty">Family &amp; Cosmetic Dentistry</p>
  <div class="icon-row">
    <svg viewBox="0 0 20 20" aria-label="phone"><path d="M5 2h3l1.5 4-2 1.5a10 10 0 0 0 5 5L14 10.5l4 1.5v3c0 1-1 2-2 2A14 14 0 0 1 3 4c0-1 1-2 2-2z"/></svg>
    <svg viewBox="0 0 20 20" aria-label="fax"><path d="M5 2h8l2 2v4H5zM2 8h16v8H2zm3 6h10v4H5z"/></svg>
    <svg viewBox="0 0 20 20" aria-label="email"><path d="M2 4h16v12H2zm1.5 1.5L10 11l6.5-5.5z" fill-rule="evenodd"/></svg>
    <svg viewBox="0 0 20 20" aria-label="website"><circle cx="10" cy="10" r="8"/></svg>
  </div>
  <ul class="contact-list">
    <li>(916) 555-0142</li>
    <li>(916) 555-0178</li>
    <li>larkvaledentalcare@mail.com</li>
    <li>www.larkvaledentalcare.com</li>
    <li>2290 Granite Hollow Road</li>
    <li>Folsom, California 95631</li>
    <li><div class="divider"></div></li>
    <li>4816 Meridian Wy., Suite B,</li>
    <li>Auburn, CA 95604</li>
  </ul>
</section>

</body>
</html>
```